Infographic job advert for modern Project Management company in renewables

I want a modern eye catching infographic style job advert . The role isnt clearly defined and so I want the add to focus on qualities and expereince so i cast a broad net and see who is interested. I have an example add from Veltrax inthe brief, this is just something I found , but I'm open to better ideas, layouts etc. There is a document for some key works, valuses etc. I have included out logo files etc . Also our website is www.marondltd.example , this tells you more about the company plus you will find us on pinglehub. reading someof our posts might help. I want modern, and eye catching. I also want the end produc to be editable by myslef for future roles or if I need to try again to get the right people. The add will get posted on Pinglehub mainly.

Target Market(s)

Experienced professionals

Industry/Entity Type

Project Management, UK based, Client Project Manager

Font styles to use
Sans Serif

Requirements
Must have
• Modern, Eye catching, editable, easy to understand, and intersting
Nice to have
• Open to ideas
Should not have
• Not specific roles, no mention of package

```html
<!DOCTYPE html>
<html lang="en">
<head>
<meta charset="utf-8">
<title>Project Management Roles – Marond</title>
<link rel="stylesheet" href="https://fonts.googleapis.com/css2?family=Montserrat:wght@400;500;600;800&family=Saira+Extra+Condensed:wght@600&display=swap">
<style>
  :root {
    --brand-red: #d3343f;
    --band-grey: #6d6d6d;
    --text-grey: #676767;
    --page-white: #f7f7f8;
    --photo-dark: #4a3328;
    --photo-mid: #7a5a48;
    --photo-red: #b8323a;
    --white: #ffffff;
  }
  * { margin: 0; padding: 0; box-sizing: border-box; }
  html, body { width: 853px; height: 1200px; overflow: hidden; background: var(--page-white); }
  body { font-family: "Montserrat", sans-serif; color: var(--text-grey); }

  .advert { position: relative; width: 853px; height: 1200px; overflow: hidden;
    background: linear-gradient(180deg, #f4f4f5 0%, #fafafa 60%, #f1f1f2 100%); }

  .hero-photo { position: absolute; left: 0; top: 0; width: 853px; height: 440px;
    clip-path: polygon(0 0, 853px 0, 853px 430px, 0 367px);
    background:
      radial-gradient(ellipse 300px 160px at 360px 230px, var(--photo-red) 0%, rgba(184,50,58,0.6) 55%, transparent 100%),
      radial-gradient(ellipse 150px 150px at 720px 300px, rgba(40,30,26,0.55) 0%, transparent 100%),
      linear-gradient(160deg, var(--photo-mid) 0%, var(--photo-dark) 100%); }

  .brand { position: absolute; left: 22px; top: 22px; display: flex; align-items: center; gap: 8px; }
  .brand-name { font-family: "Montserrat", sans-serif; font-weight: 500; font-size: 30px;
    letter-spacing: 1px; color: var(--white); line-height: 1; }
  .brand-square { width: 22px; height: 22px; background: var(--brand-red); }

  .banner { position: absolute; left: 0; top: 0; width: 853px; height: 560px; }
  .banner-title { font-family: "Saira Extra Condensed", "Arial Narrow", sans-serif; font-weight: 600;
    font-size: 64px; fill: var(--white); filter: drop-shadow(2px 2px 2px rgba(0,0,0,0.3)); }
  .location-text { font-family: "Montserrat", sans-serif; font-weight: 600; font-size: 17px; fill: var(--white); }

  .pillar { position: absolute; left: 45px; display: flex; align-items: flex-start; gap: 22px; }
  .pillar-icon { width: 44px; height: 44px; border-radius: 50%; background: var(--white);
    box-shadow: 0 1px 4px rgba(0,0,0,0.15); flex: none; display: flex; align-items: center; justify-content: center; }
  .pillar-heading { font-weight: 800; font-size: 20px; color: var(--brand-red); line-height: 1.1; margin-top: -4px; }
  .pillar-body { font-weight: 400; font-size: 15.5px; line-height: 1.3; margin-top: 5px; color: var(--text-grey); }

  .checklist { position: absolute; top: 822px; }
  .checklist-want { left: 64px; }
  .checklist-avoid { left: 407px; }
  .checklist-head { display: flex; align-items: center; gap: 14px; margin-left: -38px; }
  .checklist-title { font-weight: 800; font-size: 36px; line-height: 1.02; color: var(--brand-red); letter-spacing: -0.3px; white-space: nowrap; }
  .checklist-items { list-style: none; margin-top: 14px; margin-left: 46px; }
  .checklist-avoid .checklist-items { margin-left: 37px; }
  .checklist-items li { position: relative; padding-left: 16px; font-size: 15.5px; line-height: 34px;
    text-transform: uppercase; color: var(--text-grey); white-space: nowrap; }
  .checklist-items li::before { content: ""; position: absolute; left: 0; top: 16px; width: 3px; height: 3px;
    border-radius: 50%; background: var(--text-grey); }

  .website { position: absolute; right: 33px; top: 1160px; font-size: 13px; color: var(--brand-red); letter-spacing: 0.2px; }
</style>
</head>
<body>
<main class="advert">
  <div class="hero-photo" role="img" aria-label="Photograph of a red notebook and pen on a wooden desk, with a cube of key words: programmes, enthusiasm, experience, construction, electrical design, grid connection, renewables, battery storage, PV schemes, CDM planning"></div>

  <div class="brand">
    <span class="brand-name">MAROND</span>
    <span class="brand-square"></span>
  </div>

  <svg class="banner" viewBox="0 0 853 560" role="group" aria-label="Project Management Roles, location UK wide">
    <polygon points="22,463 853,526 853,548 60,490 60,486 22,486" fill="var(--band-grey)"/>
    <polygon points="0,365 853,428 853,526 0,463" fill="var(--brand-red)"/>
    <text class="banner-title" x="31" y="445" textLength="597" lengthAdjust="spacingAndGlyphs"
          transform="rotate(4.3 31 445)">PROJECT MANAGEMENT ROLES</text>
    <g transform="rotate(4.3 661 450)">
      <path d="M674 448c-6.6 0-12 5.4-12 12 0 9 12 27 12 27s12-18 12-27c0-6.6-5.4-12-12-12z" fill="var(--white)"/>
      <circle cx="674" cy="460" r="5" fill="var(--brand-red)"/>
      <text class="location-text" x="700" y="470" textLength="98" lengthAdjust="spacingAndGlyphs">LOCATION</text>
      <text class="location-text" x="699" y="491" textLength="75" lengthAdjust="spacingAndGlyphs">UK WIDE</text>
    </g>
  </svg>

  <section class="pillar" style="top:544px">
    <div class="pillar-icon">
      <svg width="30" height="30" viewBox="0 0 30 30" fill="none" stroke="var(--brand-red)" stroke-width="1.4" aria-hidden="true">
        <circle cx="15" cy="15" r="10"/><circle cx="15" cy="15" r="5.5"/>
        <path d="M15 1v6M15 23v6M1 15h6M23 15h6"/><path d="M12.5 15l2 2 3.5-4"/>
      </svg>
    </div>
    <div>
      <h2 class="pillar-heading">CULTURE</h2>
      <p class="pillar-body">Relaxed, Hardworking, Open to ideas, Focused on results</p>
    </div>
  </section>

  <section class="pillar" style="top:617px">
    <div class="pillar-icon">
      <svg width="30" height="30" viewBox="0 0 30 30" fill="none" stroke="var(--brand-red)" stroke-width="1.4" aria-hidden="true">
        <circle cx="15" cy="12" r="9"/><circle cx="15" cy="12" r="6"/>
        <path d="M15 8.5l1.1 2.3 2.4.3-1.8 1.6.5 2.4-2.2-1.2-2.2 1.2.5-2.4-1.8-1.6 2.4-.3z"/>
        <path d="M9 19l-3 8 3.5-1.5L11 29l3-8M21 19l3 8-3.5-1.5L19 29l-3-8"/>
      </svg>
    </div>
    <div>
      <h2 class="pillar-heading">VALUES</h2>
      <p class="pillar-body">Integrity, Quality, Communication, Detail</p>
    </div>
  </section>

  <section class="pillar" style="top:694px">
    <div class="pillar-icon">
      <svg width="30" height="30" viewBox="0 0 30 30" fill="none" stroke="var(--brand-red)" stroke-width="1.4" aria-hidden="true">
        <path d="M15 2c4 3 5 8 5 12v8h-10v-8c0-4 1-9 5-12z"/><circle cx="15" cy="11" r="2.2"/>
        <path d="M10 16l-4 4v5l4-3M20 16l4 4v5l-4-3M12 25l1 3M18 25l-1 3M15 25v3"/>
      </svg>
    </div>
    <div>
      <h2 class="pillar-heading">POTENTIAL</h2>
      <p class="pillar-body">Define your role, Enjoy your job, What you put in shapes what you get back,<br>Shape the business</p>
    </div>
  </section>

  <section class="checklist checklist-want">
    <div class="checklist-head">
      <svg width="66" height="66" viewBox="0 0 66 66" aria-hidden="true">
        <circle cx="33" cy="33" r="32" fill="none" stroke="var(--band-grey)" stroke-width="1"/>
        <circle cx="34" cy="33" r="30" fill="var(--brand-red)"/>
        <path d="M20 34l9 9 17-18" fill="none" stroke="var(--white)" stroke-width="3"/>
      </svg>
      <h2 class="checklist-title">THINGS<br>WE WANT</h2>
    </div>
    <ul class="checklist-items">
      <li>Thinkers</li><li>Doers</li><li>Listeners</li><li>Attention to details</li>
      <li>Team players</li><li>Embraces a challenge</li><li>Can do people</li>
    </ul>
  </section>

  <section class="checklist checklist-avoid">
    <div class="checklist-head">
      <svg width="66" height="66" viewBox="0 0 66 66" aria-hidden="true">
        <circle cx="33" cy="33" r="32" fill="none" stroke="var(--band-grey)" stroke-width="1"/>
        <circle cx="34" cy="33" r="30" fill="var(--brand-red)"/>
        <path d="M22 21l24 24M46 21L22 45" fill="none" stroke="var(--white)" stroke-width="2.5"/>
      </svg>
      <h2 class="checklist-title">THINGS<br>WE DON’T WANT</h2>
    </div>
    <ul class="checklist-items">
      <li>Tell me what to do</li><li>That’s not my job</li><li>It doesn’t matter</li><li>I’ll get round to it</li>
    </ul>
  </section>

  <p class="website">WWW.MARONDLTD.EXAMPLE</p>
</main>
</body>
</html>
```